Business Card Design Coralgate Airflow Solutions

The Business will be centred around supply and installation of Ventilation for domestic homes and warehousing/workshops, and will be marketed as a Eco friendly means of reducing your carbon footprint and reducing energy consumption.Our suppliers will provide a range of products that will ventilate roof spaces and later will branch into to air transfer within homes for cooling and heating other rooms of the home etc.I would like to see colours that would be commensurate with the logo provided and yet not dominate the logo.Final design should convey a Diverse , professional but friendly service that will suit client needs

Target Market(s)

Domestic home owners and warehousing/workshop businesses

Industry/Entity Type

Business

Contact Information for Business Card

Company Name: Coralgate Airflow Solutions Pty Ltd, ABN: 42 817 359 264, Address: 27 Marrowfen Tulvanna W.A 6289, Email: dale@coralgateairflowsolutions.com.au, Mobile Number: 0461 852 309

Requirements
Nice to have
• A tract art that commensurate of the logo supplied
Should not have
• Font style that opposes logo design

```html
<!DOCTYPE html>
<html lang="en">
<head>
<meta charset="utf-8">
<title>Coralgate Airflow Solutions – Business Card</title>
<link rel="stylesheet" href="https://fonts.googleapis.com/css2?family=Lato:wght@400;700&display=swap">
<style>
  :root {
    --brand-green: #14b04c;
    --brand-green-deep: #0fa845;
    --paper: #ffffff;
    --paper-shade: #e9eaea;
    --stage: #eeeae4;
    --ink-light: #ffffff;
    --card-shadow: rgba(0, 0, 0, 0.18);
  }
  * { box-sizing: border-box; margin: 0; padding: 0; }
  html, body {
    width: 1200px;
    height: 900px;
    overflow: hidden;
  }
  body {
    background: var(--stage);
    font-family: "Lato", Arial, sans-serif;
    position: relative;
  }
  .card {
    position: absolute;
    width: 540px;
    height: 310px;
    border-radius: 3px;
    overflow: hidden;
    box-shadow: 0 10px 26px var(--card-shadow);
  }
  /* Front face */
  .card-front {
    left: 40px;
    top: 295px;
    background: var(--brand-green);
    display: flex;
    align-items: center;
    justify-content: center;
  }
  .brand-name {
    font-family: "Lato", Arial, sans-serif;
    font-weight: 400;
    letter-spacing: 0.5px;
    white-space: nowrap;
    display: flex;
    align-items: center;
    gap: 10px;
  }
  .brand-mark {
    width: 12px;
    height: 12px;
    display: inline-block;
  }
  .card-front .brand-name {
    color: var(--ink-light);
    font-size: 30px;
  }
  .card-front .brand-mark { background: var(--ink-light); }

  /* Back face */
  .card-back {
    left: 620px;
    top: 295px;
    background: var(--brand-green-deep);
  }
  .back-header {
    height: 168px;
    background: radial-gradient(ellipse at 60% 40%, var(--paper) 45%, var(--paper-shade) 100%);
    display: flex;
    align-items: center;
    justify-content: center;
    padding-top: 30px;
  }
  .card-back .brand-name {
    color: var(--brand-green);
    font-size: 27px;
  }
  .card-back .brand-mark { background: var(--brand-green); }

  .back-details {
    display: flex;
    padding: 16px 0 0 0;
    color: var(--ink-light);
  }
  .person {
    width: 272px;
    text-align: right;
    padding-right: 22px;
  }
  .person-name {
    font-size: 21px;
    font-weight: 700;
    line-height: 1.15;
  }
  .person-role {
    font-size: 14px;
    margin-top: 3px;
  }
  .person-address {
    font-size: 15px;
    line-height: 1.35;
    margin-top: 10px;
  }
  .contact-list {
    list-style: none;
    font-size: 14px;
    line-height: 1;
  }
  .contact-list li {
    display: flex;
    align-items: center;
    gap: 7px;
    height: 24px;
  }
  .contact-icon {
    width: 15px;
    height: 15px;
    flex: none;
  }
</style>
</head>
<body>

  <section class="card card-front" aria-label="Business card front">
    <div class="brand-name"><span class="brand-mark"></span>Coralgate Airflow Solutions</div>
  </section>

  <section class="card card-back" aria-label="Business card back">
    <header class="back-header">
      <div class="brand-name"><span class="brand-mark"></span>Coralgate Airflow Solutions</div>
    </header>

    <div class="back-details">
      <div class="person">
        <p class="person-name">Dale Harwick</p>
        <p class="person-role">Managing Director</p>
        <p class="person-address">1234, Address GoesHere<br>Country, 12345</p>
      </div>

      <ul class="contact-list">
        <li>
          <svg class="contact-icon" viewBox="0 0 16 16" aria-hidden="true">
            <rect width="16" height="16" rx="2" fill="#fff"/>
            <path d="M3.5 8.5 Q3.5 5 8 5 Q12.5 5 12.5 8.5 L10.5 8.5 L10.5 7.2 Q8 6.5 5.5 7.2 L5.5 8.5 Z M5 9.5 H11 L11.5 12 H4.5 Z" fill="#0fa845"/>
          </svg>
          <span>123-456-7890</span>
        </li>
        <li>
          <svg class="contact-icon" viewBox="0 0 16 16" aria-hidden="true">
            <rect width="16" height="16" rx="2" fill="#fff"/>
            <rect x="4" y="3" width="8" height="10" rx="1" fill="none" stroke="#0fa845" stroke-width="1.4"/>
            <rect x="6" y="10.5" width="4" height="1.2" fill="#0fa845"/>
          </svg>
          <span>123-456-7890</span>
        </li>
        <li>
          <svg class="contact-icon" viewBox="0 0 16 16" aria-hidden="true">
            <rect width="16" height="16" rx="2" fill="#fff"/>
            <rect x="3" y="4.5" width="10" height="7" fill="none" stroke="#0fa845" stroke-width="1.3"/>
            <path d="M3 4.5 L8 8.5 L13 4.5" fill="none" stroke="#0fa845" stroke-width="1.3"/>
          </svg>
          <span>info@coralgatemail.com</span>
        </li>
        <li>
          <svg class="contact-icon" viewBox="0 0 16 16" aria-hidden="true">
            <rect width="16" height="16" rx="2" fill="#fff"/>
            <path d="M6.5 9.5 L9.5 6.5 M7 5 L8.2 3.8 A2.2 2.2 0 0 1 12.2 7.8 L11 9 M9 11 L7.8 12.2 A2.2 2.2 0 0 1 3.8 8.2 L5 7" fill="none" stroke="#0fa845" stroke-width="1.4" stroke-linecap="round"/>
          </svg>
          <span>www.coralgateweb.com</span>
        </li>
      </ul>
    </div>
  </section>

</body>
</html>
```